Album Cover Art

Need an album cover artwork for my up and coming album titled LUMERIVO. Themes would include underwater landscapes, dream like trippy visuals and deep oceanic colours. Psychedelic styles and Drug fuelled awakenings scuba divers garden scenes etc. My artist Name is Kettles !
Track titles for the album for Inspiration
Velvet Kite
Copper Hymn
Mr Pebble
Paper Sled
Lumerivo
Ashfalls
Valley of Clocks
Tower of Ladders
The Nooks
Bell Ringer
I have included 3 off the tracks to listen to for Inspiration and reference artworks.
Updates
Target Market(s)
Specifically for digital streaming websites not a hard copy.

```html
<!DOCTYPE html>
<html lang="en">
<head>
<meta charset="utf-8">
<title>Lumerivo — Kettles</title>
<link href="https://fonts.googleapis.com/css2?family=Playfair+Display:wght@700&family=Caveat+Brush&display=swap" rel="stylesheet">
<style>
  :root {
    --backdrop: #efb8e6;
    --frame-white: #ffffff;
    --deep-navy: #1b2466;
    --reef-teal: #2b8fb0;
    --reef-cyan: #5cc6e0;
    --coral-yellow: #e9c02e;
    --coral-red: #d4533a;
    --kelp-green: #2f7a52;
  }
  html, body {
    margin: 0;
    padding: 0;
    width: 750px;
    height: 1200px;
    overflow: hidden;
    background: var(--backdrop);
  }
  .canvas {
    position: relative;
    width: 750px;
    height: 1200px;
  }
  .album-cover {
    position: absolute;
    left: 75px;
    top: 300px;
    width: 600px;
    height: 600px;
    overflow: hidden;
  }
  .reef-photo {
    position: absolute;
    inset: 0;
    background:
      radial-gradient(circle at 88% 88%, var(--coral-red) 0, transparent 18%),
      radial-gradient(circle at 30% 75%, var(--coral-yellow) 0, transparent 26%),
      radial-gradient(circle at 65% 45%, var(--coral-yellow) 0, transparent 18%),
      radial-gradient(circle at 15% 95%, var(--coral-yellow) 0, transparent 22%),
      radial-gradient(circle at 75% 95%, var(--coral-yellow) 0, transparent 20%),
      radial-gradient(circle at 45% 70%, var(--reef-cyan) 0, transparent 22%),
      radial-gradient(circle at 20% 20%, var(--reef-teal) 0, transparent 30%),
      radial-gradient(circle at 80% 35%, var(--kelp-green) 0, transparent 22%),
      radial-gradient(circle at 40% 5%, var(--coral-red) 0, transparent 12%),
      var(--deep-navy);
  }
  .cover-frame {
    position: absolute;
    left: 15px;
    top: 15px;
    right: 15px;
    bottom: 15px;
    border: 7px solid var(--frame-white);
  }
  .album-title {
    position: absolute;
    left: 0;
    right: 0;
    top: 22px;
    margin: 0;
    text-align: center;
    font-family: "Playfair Display", Georgia, serif;
    font-weight: 700;
    font-size: 128px;
    line-height: 1;
    letter-spacing: -2px;
    color: var(--frame-white);
  }
  .artist-credit {
    position: absolute;
    right: 52px;
    top: 470px;
    margin: 0;
    font-family: "Caveat Brush", cursive;
    font-size: 50px;
    line-height: 1;
    color: var(--frame-white);
  }
</style>
</head>
<body>
  <main class="canvas">
    <section class="album-cover">
      <div class="reef-photo" role="img" aria-label="Photograph of a vivid coral reef with tropical fish, yellow and red corals and deep blue water"></div>
      <div class="cover-frame"></div>
      <h1 class="album-title">Lumerivo</h1>
      <p class="artist-credit">by Kettles</p>
    </section>
  </main>
</body>
</html>
```